Car Wrap Design - Architectural Homes

We are looking for a design for a branded vehicle for an architectural modular housing company. Our company is minimalistic, modern, and contemporary. Brand guidelines attached.
Vehicle is : Ordel Kastor lumina 2021
Vehicle is black

Note, we would like to outline our services including "Architectural Modular Homes"
No colour to be included in the design. Grey scale only please.

Industry/Entity Type

architectural odular housing

Colors

Designer to choose only greyscale colors for use in the design.

Requirements
Should not have
• colour

```html
<!DOCTYPE html>
<html lang="en">
<head>
<meta charset="utf-8">
<title>Alcove – Vehicle Wrap Side Panel</title>
<link href="https://fonts.googleapis.com/css2?family=Inter:wght@300;400&display=swap" rel="stylesheet">
<style>
  :root {
    --page: #ffffff;
    --body-black: #0b0b0b;
    --wrap-grey: #b9b9b9;
    --text-light: #d6d6d6;
  }
  html, body {
    margin: 0;
    padding: 0;
    width: 1200px;
    height: 1200px;
    overflow: hidden;
    background: var(--page);
    font-family: "Inter", Helvetica, Arial, sans-serif;
  }
  .canvas {
    position: relative;
    width: 1200px;
    height: 1200px;
  }
  .wrap-panel {
    position: absolute;
    left: 150px;
    top: 500px;
    width: 950px;
    height: 215px;
    background: var(--body-black);
    border-radius: 14px 22px 10px 10px;
    overflow: hidden;
  }
  .brand-strip {
    position: absolute;
    left: 46px;
    top: 44px;
    display: flex;
    align-items: center;
    gap: 12px;
    color: var(--text-light);
  }
  .brand-name {
    font-size: 15px;
    font-weight: 400;
    letter-spacing: 0.02em;
  }
  .services {
    font-size: 7.5px;
    line-height: 1.05;
    font-weight: 400;
  }
  .divider {
    width: 2px;
    height: 22px;
    background: var(--text-light);
  }
  .web-address {
    font-size: 13.5px;
    font-weight: 300;
  }
  .hero-wordmark {
    position: absolute;
    left: 300px;
    top: 95px;
    margin: 0;
    font-size: 168px;
    font-weight: 300;
    line-height: 1;
    letter-spacing: -0.03em;
    color: var(--wrap-grey);
  }
</style>
</head>
<body>
  <main class="canvas">
    <section class="wrap-panel" aria-label="Vehicle side wrap">
      <div class="brand-strip">
        <span class="brand-name">Alcove</span>
        <span class="services">Modular<br>Architectural<br>Homes</span>
        <span class="divider"></span>
        <span class="web-address">alcovehomes.co.nz</span>
      </div>
      <p class="hero-wordmark">Alcove</p>
    </section>
  </main>
</body>
</html>
```